Banner for a National Dental Conference

We need a banner logo for our next Dental Conference in 2017. Our theme is 'Challenging the Status Quo'.
It must have the words '20 years of oral health therapy in Victoria' and the conference date and venue:
7-8th April 2017
Wattlebrook Shore Lodge, Torquay, Victoria.
It must also feature our association logo as attached.
Please be creative, however, we would like a 'clean' design, not cluttered.
The design is intended for use in the conference program and website.

Target Market(s)

Dental practitioners

Industry/Entity Type

Dental

Requirements
Must have
• As above.

```html
<!DOCTYPE html>
<html lang="en">
<head>
<meta charset="utf-8">
<title>Challenging the Status Quo – Conference Banner</title>
<link rel="stylesheet" href="https://fonts.googleapis.com/css2?family=Ubuntu:wght@400;700&family=Oswald:wght@500;600&display=swap">
<style>
  :root {
    --purple: #5b2f98;
    --green: #22a985;
    --page: #f2f2f2;
    --white: #ffffff;
    --panel-grey: #ececec;
  }
  html, body {
    margin: 0;
    width: 1200px;
    height: 1200px;
    overflow: hidden;
    background: var(--page);
  }
  .banner {
    position: absolute;
    left: 17px;
    top: 418px;
    width: 1166px;
    height: 365px;
    overflow: hidden;
    background: linear-gradient(180deg, var(--white) 0%, var(--panel-grey) 100%);
  }
  .banner-shapes {
    position: absolute;
    inset: 0;
  }
  .portrait-photo {
    position: absolute;
    right: 0;
    top: 0;
    width: 181px;
    height: 365px;
    background: linear-gradient(160deg, #c9a06a 0%, #e8c4a6 45%, #f1dccb 75%, #d9b193 100%);
  }
  .theme-title {
    position: absolute;
    left: 94px;
    top: 52px;
    margin: 0;
    font-family: "Ubuntu", sans-serif;
    font-weight: 700;
    font-size: 48px;
    line-height: 1;
    white-space: nowrap;
    color: var(--white);
  }
  .theme-subtitle {
    position: absolute;
    left: 98px;
    top: 114px;
    margin: 0;
    font-family: "Ubuntu", sans-serif;
    font-weight: 700;
    font-size: 31px;
    line-height: 1;
    white-space: nowrap;
    color: var(--white);
  }
  .event-date {
    position: absolute;
    left: 86px;
    top: 210px;
    margin: 0;
    font-family: "Oswald", sans-serif;
    font-weight: 600;
    font-size: 60px;
    line-height: 1;
    letter-spacing: -0.5px;
    white-space: nowrap;
    color: var(--green);
  }
  .event-venue {
    position: absolute;
    left: 86px;
    top: 283px;
    margin: 0;
    font-family: "Oswald", sans-serif;
    font-weight: 500;
    font-size: 21px;
    line-height: 1;
    white-space: nowrap;
    color: var(--purple);
  }
  .association-name {
    position: absolute;
    left: 690px;
    top: 262px;
    display: flex;
    align-items: center;
    gap: 12px;
    font-family: "Ubuntu", sans-serif;
    font-weight: 700;
    font-size: 40px;
    line-height: 1;
    white-space: nowrap;
    color: var(--green);
  }
  .association-mark {
    width: 22px;
    height: 22px;
    background: var(--green);
  }
</style>
</head>
<body>
  <section class="banner">
    <svg class="banner-shapes" viewBox="0 0 1166 365" width="1166" height="365">
      <defs>
        <linearGradient id="titleFill" x1="0" y1="0" x2="1" y2="1">
          <stop offset="0" stop-color="#4e2688"/>
          <stop offset="1" stop-color="#7047b3"/>
        </linearGradient>
        <linearGradient id="toolsFill" x1="0" y1="0" x2="1" y2="1">
          <stop offset="0" stop-color="#ffffff"/>
          <stop offset="1" stop-color="#d8dcdc"/>
        </linearGradient>
        <filter id="softGlow" x="-20%" y="-20%" width="140%" height="140%">
          <feDropShadow dx="0" dy="2" stdDeviation="5" flood-color="#000" flood-opacity="0.18"/>
        </filter>
      </defs>

      <path class="frame-left" d="M0 0 H38 C18 70 20 270 62 340 H0 Z" fill="#22a985"/>
      <rect class="frame-bottom" x="0" y="338" width="995" height="27" fill="#22a985"/>

      <rect class="title-panel" x="58" y="32" width="770" height="144" rx="44" fill="url(#titleFill)" stroke="#22a985" stroke-width="5"/>

      <path class="swoosh-green" d="M880 0 H898 C890 70 850 120 770 160 C660 210 560 240 520 340 H505 C540 230 640 200 750 150 C840 110 875 60 880 0 Z" fill="#22a985"/>
      <path class="swoosh-purple" d="M898 0 H938 C930 80 885 130 800 170 C690 220 610 250 590 340 H520 C560 240 660 210 770 160 C850 120 890 70 898 0 Z" fill="#5b2f98"/>
      <path class="swoosh-green-inner" d="M800 170 C690 220 610 250 590 340 H610 C630 260 700 230 805 180 Z" fill="#22a985"/>

      <circle cx="848" cy="120" r="108" fill="#ffffff" filter="url(#softGlow)"/>
      <circle cx="848" cy="120" r="95" fill="#ffffff" stroke="#22a985" stroke-width="6"/>
      <circle class="instruments-photo" role="img" aria-label="Photo of a toothbrush and dental hand instruments" cx="848" cy="120" r="88" fill="url(#toolsFill)"/>
    </svg>

    <div class="portrait-photo" role="img" aria-label="Photo of a smiling woman with curly blonde hair"></div>

    <h1 class="theme-title">Challenging the Status Quo</h1>
    <p class="theme-subtitle">20 years of oral health therapy in Victoria</p>
    <p class="event-date">7-8TH APRIL 2017</p>
    <p class="event-venue">WATTLEBROOK SHORE LODGE, TORQUAY, VICTORIA</p>

    <div class="association-name"><span class="association-mark"></span>Oralis Guild</div>
  </section>
</body>
</html>
```